A professional I.T consulting company requires a web design

Our company needs a fresh web design to help us drive our business forward. We are an Information Technology company who specialises in solutions based I.T delivery and consultations and who prides ourselves on our professional approach to business.

We would like a web site design from a designer who may be able to help us upload the site to WordPress and who may be interested in completing the "coding" section of the site (minimal coding). Although this is not essential to this project and won't factor into the decision making process.

A very thorough brief has been put together for this design project so very limited work is required in regards to content (the brief sets out all the content text - copy write material).

Please see the attached project documents for a copy of the brief

Target Market(s)

Please refer to the attached brief

Industry/Entity Type

Business

Requirements
Must have
• Please refer to the attached brief
Nice to have
Should not have

```html
<!DOCTYPE html>
<html lang="en">
<head>
<meta charset="utf-8">
<title>NORVITS – IT Support & Solutions</title>
<link href="https://fonts.googleapis.com/css2?family=Signika:wght@300;400;600&family=Lato:ital,wght@0,400;0,700;1,400&display=swap" rel="stylesheet">
<style>
:root{
  --blue:#3a9fd9;
  --blue-dark:#2a86c0;
  --ink:#333;
  --muted:#666;
  --nav:#2f2f2f;
  --panel:#f2f2f2;
  --support:#6b6b6b;
  --footer:#3b3b3b;
}
*{box-sizing:border-box;margin:0;padding:0}
html,body{width:917px;height:1200px;overflow:hidden;background:#fff}
body{position:relative;font-family:"Lato",sans-serif;color:var(--ink)}
.abs{position:absolute}

.brand{left:100px;top:14px}
.brand-name{font-family:"Signika",sans-serif;font-weight:600;font-size:24px;color:var(--blue);line-height:1}
.brand-tag{margin-top:2px;font-size:5.5px;letter-spacing:.8px;color:#888;text-transform:uppercase}
.call{left:618px;top:23px;display:flex;align-items:center;gap:6px;font-size:10px;color:#555}
.call strong{font-family:"Signika",sans-serif;font-weight:400;color:var(--blue);font-size:14px}
.search{left:787px;top:19px;width:30px;height:27px;background:#eee;display:flex;align-items:center;justify-content:center}

.nav{left:0;top:63px;width:917px;height:38px;background:linear-gradient(#3a3a3a,#262626)}
.nav a{position:absolute;top:13px;font-size:10px;color:#ddd;text-decoration:none}
.nav a.active{color:var(--blue)}

.hero{left:0;top:101px;width:917px;height:296px;background:linear-gradient(90deg,#6b6d70 0%,#9a9da1 45%,#7a7c80 75%,#3a3c40 100%)}
.hero h1{position:absolute;left:100px;top:54px;font-family:"Signika",sans-serif;font-weight:300;font-size:27px;line-height:46px;color:#fff}
.hero p{position:absolute;left:100px;top:138px;width:240px;font-family:"Signika",sans-serif;font-weight:300;font-size:13px;line-height:18.5px;color:#fff}
.hero .btn{position:absolute;left:101px;top:210px;width:91px;height:29px;background:var(--blue);border-bottom:3px solid var(--blue-dark);color:#fff;font-family:"Signika",sans-serif;font-size:10px;display:flex;align-items:center;justify-content:center}
.hero .visual{position:absolute;left:330px;top:0;width:587px;height:296px;background:radial-gradient(circle at 45% 45%,rgba(255,255,255,.35),rgba(255,255,255,0) 60%)}
.arrow{position:absolute;top:131px}

.feature{top:433px;width:229px;height:112px;background:var(--blue);border-bottom:2px solid var(--blue-dark);color:#fff;padding:10px}
.feature h3{position:absolute;left:70px;top:18px;font-family:"Signika",sans-serif;font-weight:400;font-size:15px}
.feature p{position:absolute;left:10px;top:53px;width:215px;font-size:8.5px;line-height:13.5px}
.feature .more{position:absolute;left:11px;top:88px;font-size:8.5px;font-style:italic}
.feature svg{position:absolute;left:9px;top:7px}

.welcome h2{font-family:"Signika",sans-serif;font-weight:300;font-size:16px;color:#333}
.photo{background:linear-gradient(135deg,#d8dde2,#a9b0b8)}
.welcome-text{left:282px;top:610px;width:355px;font-size:8.3px;line-height:14px;color:#666}
.btn-sm{background:var(--blue);color:#fff;font-family:"Signika",sans-serif;font-size:9px;display:flex;align-items:center;justify-content:center}

.support{left:650px;top:578px;width:168px;height:146px;background:var(--support);color:#fff;padding:12px 19px}
.support h3{font-family:"Signika",sans-serif;font-weight:300;font-size:15px;margin-bottom:12px}
.support li{list-style:none;display:flex;align-items:center;gap:14px;height:24px;font-family:"Signika",sans-serif;font-weight:300;font-size:9.5px}
.support li i{width:13px;height:13px;display:flex;align-items:center;justify-content:center}

.card{top:746px;width:230px;height:228px;background:var(--panel);padding:0 12px}
.card h3{margin-top:16px;font-family:"Signika",sans-serif;font-weight:300;font-size:16px;color:#333;padding-left:3px}
.card .photo{margin-top:8px;height:104px}
.card p{margin-top:13px;font-size:8.3px;line-height:14px;color:#666}
.card .more{position:absolute;left:13px;top:205px;font-size:8.5px;font-style:italic;color:var(--blue)}
.quote{font-size:8.2px;line-height:14.5px;font-style:italic;color:#777;margin-top:12px;padding:0 2px}
.author{position:absolute;right:74px;top:164px;text-align:right;font-size:8.3px;line-height:16px;color:#888;font-style:italic}
.author b{font-style:normal;font-weight:400;color:var(--blue);font-size:9.5px}
.avatar{position:absolute;right:17px;top:163px;width:46px;height:46px;background:linear-gradient(135deg,#c9b6a4,#8a7564)}

.clients-title{left:101px;top:1008px;font-family:"Signika",sans-serif;font-weight:300;font-size:16px}
.pager{top:1011px;width:18px;height:18px;display:flex;align-items:center;justify-content:center}
.client{top:1052px;display:flex;align-items:center;gap:5px;font-family:"Signika",sans-serif;font-weight:600;font-size:16px;color:#2a5c9a}
.client span.dot{width:13px;height:13px;border-radius:50%;background:currentColor}

.footer{left:0;top:1124px;width:917px;height:76px;background:var(--footer)}
.footer p{position:absolute;left:101px;top:26px;font-size:9.5px;color:#ccc}
.social{position:absolute;top:27px;width:21px;height:21px;border-radius:50%;background:#bdbdbd}
</style>
</head>
<body>

<header>
  <div class="abs brand">
    <div class="brand-name">NORVITS</div>
    <div class="brand-tag">Clear answers, real support</div>
  </div>
  <div class="abs call">
    <svg width="20" height="20" viewBox="0 0 20 20"><circle cx="10" cy="10" r="9" fill="none" stroke="#555" stroke-width="1.2"/><path d="M7 6l2 2-1 1.5c.6 1.2 1.4 2 2.5 2.5L12 11l2 2-1.3 1.2C9.5 14 6 10.5 5.8 7.3z" fill="#555"/></svg>
    Call Us : <strong>1300 555 201</strong>
  </div>
  <div class="abs search">
    <svg width="12" height="12" viewBox="0 0 12 12"><circle cx="5" cy="5" r="3.6" fill="none" stroke="#555" stroke-width="1.6"/><path d="M7.6 7.6l3 3" stroke="#555" stroke-width="1.8"/></svg>
  </div>
</header>

<nav class="abs nav">
  <a class="active" style="left:117px">Home</a>
  <a style="left:186px">About Us</a>
  <a style="left:271px">Why NORVITS?</a>
  <a style="left:379px">Services</a>
  <a style="left:459px">Solutions</a>
  <a style="left:549px">Technologies</a>
  <a style="left:655px">Contact Us</a>
</nav>

<section class="abs hero">
  <div class="visual" role="img" aria-label="Businessman holding a tablet with a connected globe network graphic"></div>
  <h1>We Succeed,<br>When you succeed..</h1>
  <p>Our business is simple, provide you the best solution &amp; supports possible to achive your goals.</p>
  <div class="btn">Learn More &gt;&gt;</div>
  <svg class="arrow" style="left:64px" width="16" height="26" viewBox="0 0 16 26"><path d="M13 2L3 13l10 11" fill="none" stroke="#333" stroke-width="4"/></svg>
  <svg class="arrow" style="left:842px" width="16" height="26" viewBox="0 0 16 26"><path d="M3 2l10 11L3 24" fill="none" stroke="#fff" stroke-width="4"/></svg>
</section>

<section>
  <div class="abs feature" style="left:100px">
    <svg width="50" height="36" viewBox="0 0 50 36"><circle cx="14" cy="22" r="9" fill="none" stroke="#fff" stroke-width="4" stroke-dasharray="3 2.5"/><circle cx="14" cy="22" r="4" fill="#fff"/><circle cx="36" cy="10" r="6" fill="none" stroke="#fff" stroke-width="3" stroke-dasharray="2.5 2"/><circle cx="26" cy="14" r="3" fill="none" stroke="#fff" stroke-width="2"/></svg>
    <h3>SERVICES</h3>
    <p>Neque porro quisquam est qui dolorem ipsum quia dolor sit amet, consectetur, adipisci velit..</p>
    <span class="more">View More &gt;&gt;</span>
  </div>
  <div class="abs feature" style="left:344px">
    <svg width="40" height="40" viewBox="0 0 40 40"><path d="M18 3a11 11 0 0 0-6 20v5h12v-5a11 11 0 0 0-6-20z" fill="#fff"/><rect x="12" y="30" width="12" height="2.5" fill="#fff"/><rect x="13" y="34" width="10" height="2.5" fill="#fff"/></svg>
    <h3 style="left:59px;top:20px">SOLUTION</h3>
    <p>Neque porro quisquam est qui dolorem ipsum quia dolor sit amet, consectetur, adipisci velit..</p>
    <span class="more">View More &gt;&gt;</span>
  </div>
  <div class="abs feature" style="left:589px">
    <svg width="44" height="40" viewBox="0 0 44 40"><rect x="8" y="6" width="28" height="19" rx="1" fill="none" stroke="#fff" stroke-width="2"/><path d="M3 29h38l-3 4H6z" fill="none" stroke="#fff" stroke-width="2"/><circle cx="22" cy="14" r="4" fill="none" stroke="#fff" stroke-width="1.6"/><path d="M22 16v6" stroke="#fff" stroke-width="1.6"/></svg>
    <h3 style="left:69px;top:21px">TECHNOLOGY</h3>
    <p>Neque porro quisquam est qui dolorem ipsum quia dolor sit amet, consectetur, adipisci velit..</p>
    <span class="more">View More &gt;&gt;</span>
  </div>
</section>

<section class="welcome">
  <h2 class="abs" style="left:100px;top:575px">Welcome to Our Website Mainpage..</h2>
  <div class="abs photo" style="left:99px;top:607px;width:168px;height:103px" role="img" aria-label="Smiling businesswoman in an office"></div>
  <p class="abs welcome-text">NORVITS provides quality Information Technology support and solutions services for businesses throughout the Latrobe Valley and the greater Metropolitan areas. We pr-ourselves on our professional approach to our service delivery and in our no-nonse-nse approach to meeting our client's unique business I.T needs.</p>
  <div class="abs btn-sm" style="left:283px;top:685px;width:62px;height:22px">More &gt;&gt;</div>
</section>

<aside class="abs support">
  <h3>Support Links</h3>
  <ul>
    <li><i><svg width="13" height="13" viewBox="0 0 13 13"><circle cx="6.5" cy="6.5" r="4.5" fill="none" stroke="#fff" stroke-width="2.4" stroke-dasharray="2 1.5"/></svg></i>Log Service Call</li>
    <li><i><svg width="13" height="13" viewBox="0 0 13 13"><rect x="1" y="1" width="6" height="8" fill="none" stroke="#fff" stroke-width="1.3"/><rect x="5" y="6" width="7" height="6" fill="none" stroke="#fff" stroke-width="1.3"/></svg></i>1300 555 208</li>
    <li><i><svg width="12" height="12"><rect x="1" y="1" width="10" height="10" fill="#fff"/></svg></i>Desktop Support</li>
    <li><i><svg width="12" height="12"><circle cx="6" cy="6" r="5" fill="#fff"/></svg></i>Laptop Support</li>
  </ul>
</aside>

<section>
  <article class="abs card" style="left:99px">
    <h3>Why Norvits ?</h3>
    <div class="photo" role="img" aria-label="People holding question mark signs" style="background:linear-gradient(135deg,#e9ecef,#9fb4c8)"></div>
    <p>Technology support and solutions services for to businesses throughout the Latrobe Valley and the greater Metropolitan areas.</p>
    <span class="more">Read More &gt;&gt;</span>
  </article>
  <article class="abs card" style="left:344px">
    <h3>About Us</h3>
    <div class="photo" role="img" aria-label="Smiling businessman with colleagues in a meeting" style="background:linear-gradient(135deg,#c9d6e3,#8fa3b8)"></div>
    <p>Technology support and solutions services for to businesses throughout the Latrobe Valley and the greater Metropolitan areas.</p>
    <span class="more">Read More &gt;&gt;</span>
  </article>
  <article class="abs card" style="left:588px">
    <h3>Testimonials</h3>
    <p class="quote"><span style="font-size:16px;color:#999;font-style:normal">&ldquo;</span> Lorem ipsum dolor sit amet, consecteturese adip elit, sed do eiusmod tempor incididse labore et dolor magna aliqua. Ut enim ad minim veniam, quis nostr exercitation ullamco laboris nisi ut aliquip ex ea com consequat. Duises aute irure dolor in reprehenderite voluptate velt esse cillum dolore...</p>
    <div class="author"><b>by Martin Caldwell</b><br>Finance Minister/ Common wealth<br>from Newyork</div>
    <div class="avatar" role="img" aria-label="Portrait of the client"></div>
  </article>
</section>

<section>
  <h2 class="abs clients-title">Our Clients</h2>
  <div class="abs pager" style="left:780px;background:#333"><svg width="8" height="8"><path d="M6 1L2 4l4 3" fill="none" stroke="#fff" stroke-width="1.6"/></svg></div>
  <div class="abs pager" style="left:800px;background:var(--blue)"><svg width="8" height="8"><path d="M2 1l4 3-4 3" fill="none" stroke="#fff" stroke-width="1.6"/></svg></div>
  <div class="abs client" style="left:103px;color:#1d6fb8"><span class="dot"></span>Corelink</div>
  <div class="abs client" style="left:212px;color:#1a5fb0"><span class="dot" style="border-radius:0"></span>Voltara</div>
  <div class="abs client" style="left:322px;color:#1c2b4a"><span class="dot"></span>Pipeline Pro</div>
  <div class="abs client" style="left:446px;color:#6b3a1f">Hollowbrook Aid</div>
  <div class="abs client" style="left:583px;color:#222">Harlow Legal</div>
  <div class="abs client" style="left:709px;color:#1f3e7a"><span class="dot"></span>bluewire</div>
</section>

<footer class="abs footer">
  <p>Copyright ©2014. norvits. All right reserved.</p>
  <span class="social" style="left:717px"></span>
  <span class="social" style="left:743px"></span>
  <span class="social" style="left:769px"></span>
  <span class="social" style="left:795px"></span>
</footer>

</body>
</html>
```